looking for sleek business card to standout from the crowd!

We are a young biotechnology company looking to help you personalize your health through understanding your genetic make up. We need you help in making a clean but sleek business card design using our new logo. The goal? Any time we give our cards out, people say "nice card!" The feel we are going for is "modern-techy". We don't want to come across as an old, giant pharma company, but not trying to be a hipster either.

Target Market(s)

healthcare and biotechnology industry.

Industry/Entity Type

Biotechnology

Contact Information for Business Card

Info to include on the card will be NAME, TITLE, EMAIL, PHONE. The companies website (www.corvalinbio.com) should also be on the card some where. Would like the logo, when printed, to be raised.

Requirements
Must have
• The logo we have attached in the color it is in. Fonts for text should lean toward more professional/tech.
Nice to have
• Prefer white/light color background
Should not have
• cartoons, landscape backgrounds images.

```html
<!DOCTYPE html>
<html lang="en">
<head>
<meta charset="utf-8">
<title>Corvalin – Business Card</title>
<link href="https://fonts.googleapis.com/css2?family=Open+Sans:wght@400;700&family=Noto+Serif:wght@400&display=swap" rel="stylesheet">
<style>
  :root {
    --backdrop: #ecebe8;
    --card-light: #ffffff;
    --card-dark: #1f2123;
    --brand-green: #7cc242;
    --ink: #111111;
    --ink-light: #f2f2f2;
    --rule-blue: #1b6fb8;
  }
  * { box-sizing: border-box; margin: 0; padding: 0; }
  html, body {
    width: 1200px; height: 801px; overflow: hidden;
    background: var(--backdrop);
    font-family: "Open Sans", Arial, sans-serif;
  }
  .canvas {
    position: relative; width: 1200px; height: 801px;
    display: flex; align-items: center; justify-content: center; gap: 40px;
  }
  .card {
    position: relative; width: 520px; height: 297px;
    box-shadow: 0 6px 18px rgba(0,0,0,0.18);
  }
  .card--front { background: var(--card-light); }
  .card--back {
    background: var(--card-dark);
    display: flex; align-items: center; justify-content: center;
  }
  .company-name {
    font-family: "Open Sans", Arial, sans-serif;
    font-weight: 400; line-height: 1; white-space: nowrap;
  }
  .card--front .company-name {
    position: absolute; left: 34px; top: 130px;
    width: 230px; text-align: center;
    font-size: 34px; color: var(--ink);
  }
  .card--back .company-name { font-size: 44px; color: var(--ink-light); }
  .divider {
    position: absolute; left: 290px; top: 74px;
    width: 2px; height: 150px; background: var(--rule-blue);
  }
  .details { position: absolute; left: 316px; top: 78px; color: var(--ink); }
  .details__name { font-size: 24px; font-weight: 400; line-height: 1.1; }
  .details__name strong { font-weight: 700; }
  .details__title {
    font-family: "Noto Serif", Georgia, serif;
    color: var(--brand-green); font-size: 16px; margin-top: 2px;
  }
  .contact { list-style: none; margin-top: 16px; }
  .contact__item {
    display: flex; align-items: center; gap: 10px;
    font-size: 15px; line-height: 24px; white-space: nowrap;
  }
  .contact__icon { width: 14px; height: 14px; flex: none; }
</style>
</head>
<body>
<main class="canvas">
  <section class="card card--front" aria-label="Card front">
    <p class="company-name">Corvalin</p>
    <div class="divider"></div>
    <div class="details">
      <p class="details__name">Your <strong>Name</strong></p>
      <p class="details__title">Job Title</p>
      <ul class="contact">
        <li class="contact__item">
          <svg class="contact__icon" viewBox="0 0 16 16" aria-hidden="true"><path fill="#7cc242" d="M2 5c0-2 2-3 6-3s6 1 6 3v1h-3V4.5H5V6H2zM4 7h8l2 6H2z"/><circle cx="8" cy="10" r="1.6" fill="#fff"/></svg>
          <span>000 000 0000</span>
        </li>
        <li class="contact__item">
          <svg class="contact__icon" viewBox="0 0 16 16" aria-hidden="true"><rect x="1" y="3" width="14" height="10" fill="#7cc242"/><path d="M1 3l7 6 7-6" fill="none" stroke="#fff" stroke-width="1.4"/></svg>
          <span>youermail@xyz.com</span>
        </li>
        <li class="contact__item">
          <svg class="contact__icon" viewBox="0 0 16 16" aria-hidden="true"><g fill="none" stroke="#7cc242" stroke-width="1.3"><circle cx="8" cy="8" r="6.5"/><ellipse cx="8" cy="8" rx="3" ry="6.5"/><path d="M1.5 8h13M3 4.5h10M3 11.5h10"/></g></svg>
          <span>www.corvalinbio.com</span>
        </li>
      </ul>
    </div>
  </section>

  <section class="card card--back" aria-label="Card back">
    <p class="company-name">Corvalin</p>
  </section>
</main>
</body>
</html>
```